Velmora Diagnostics Website

Project Description – Velmora Website Design
We need a clean, modern, and professional website for Velmora Diagnostics, a Ashgrove Hollis University of Dunmere spin-out focused on early cancer detection. Our first product, GlandSURE™, is a urine-based risk assessment test for pancreatic cancer, supported by strong clinical validation and partnerships with leading hospitals.

The site should:

Communicate trust, innovation, and clinical credibility.
Feature a clear value proposition on the home page with strong calls to action for investors, clinicians, and partners.
Showcase our technology, science, and clinical evidence in a way that is accessible but authoritative.
Highlight our university heritage, team, and collaborators.
Include sections for products/services, news/press, and contact forms.
Be fully responsive, WordPress compatible, SEO-friendly, and WCAG 2.1 AA accessible.

We want a minimalist, elegant design with subtle animations, strong visuals (e.g., science/biotech imagery), and a clear structure for future growth.
Deliverables should include editable design files (Figma/Sketch/Adobe XD) and a style guide.

```html
<!DOCTYPE html>
<html lang="en">
<head>
<meta charset="utf-8">
<title>Velmora Diagnostics</title>
<link href="https://fonts.googleapis.com/css2?family=Poppins:wght@400;500;600;700&display=swap" rel="stylesheet">
<style>
:root{
  --blue:#3b86d8;
  --blue-dark:#2a6fc0;
  --blue-soft:#5aa0e6;
  --yellow:#f6c22d;
  --ink:#1b1d24;
  --text:#4a4f5a;
  --muted:#8a8f99;
  --night:#15171d;
  --card-night:#23262e;
  --white:#ffffff;
  --line:#e4e7ec;
}
*{margin:0;padding:0;box-sizing:border-box}
html,body{width:1200px;height:5384px;overflow:hidden}
body{font-family:'Poppins',sans-serif;color:var(--text);background:var(--white);position:relative}
.abs{position:absolute}
.btn{position:absolute;display:inline-block;border-radius:22px;font-size:11px;font-weight:600;letter-spacing:.5px;padding:10px 26px;text-transform:uppercase;white-space:nowrap}
.btn-blue{background:var(--blue);color:var(--white)}
.btn-yellow{background:var(--yellow);color:var(--ink)}
.btn-white{background:var(--white);color:var(--blue)}
.h2{font-size:34px;font-weight:600;color:var(--ink)}
.p{font-size:12.5px;line-height:1.7}
.photo{position:absolute;overflow:hidden}

/* header */
.site-header{position:absolute;top:0;left:0;width:1200px;height:92px;border-bottom:1px solid var(--line)}
.brand{position:absolute;display:flex;align-items:center;gap:10px;font-weight:600;font-size:22px;color:var(--blue);white-space:nowrap}
.brand .mark{width:24px;height:24px;border-radius:50%;background:var(--yellow)}
.main-nav{position:absolute;left:560px;top:34px;display:flex;gap:34px;font-size:13px;color:var(--ink)}
.main-nav .active{color:var(--blue);font-weight:600}

/* hero */
.hero-title{left:128px;top:196px;font-size:46px;line-height:1.18;font-weight:700;color:var(--ink);width:560px}
.hero-stripe{left:0;top:576px;width:1200px;height:6px;background:linear-gradient(90deg,var(--yellow),var(--blue) 40%,#e25c5c 70%,var(--yellow))}

/* product */
.product{left:0;top:1100px;width:1200px;height:600px;background:var(--blue)}
.feature{position:absolute;border-radius:10px;padding:18px 20px;color:var(--ink)}
.feature h3{font-size:16px;font-weight:600;margin-bottom:6px}
.feature p{font-size:10.5px;line-height:1.55}
.product-name{left:730px;top:1364px;font-size:60px;font-weight:500;color:var(--white);white-space:nowrap}

/* testimonials */
.testimonials{left:0;top:3460px;width:1200px;height:620px;background:var(--night)}
.t-card{position:absolute;top:3620px;width:240px;height:310px;background:var(--card-night);border-radius:10px;padding:26px 22px;color:#cfd2d8}
.t-card .avatar{width:46px;height:46px;border-radius:50%;background:#5c6270;margin-bottom:18px}
.t-card p{font-size:11px;line-height:1.7;margin-bottom:30px}
.t-card .name{font-size:12px;color:var(--white);font-weight:600}
.t-card .role{font-size:10px;color:var(--muted)}
.arrow{position:absolute;top:3760px;width:30px;height:30px;border-radius:50%;background:var(--blue)}

/* news */
.news-card{position:absolute;top:4420px;width:420px}
.news-card .img{height:210px;border-radius:6px}
.news-card .meta{font-size:10px;color:var(--muted);margin:14px 0 6px}
.news-card h4{font-size:17px;font-weight:600;color:var(--ink);line-height:1.35}
.news-card p{font-size:11px;line-height:1.6;margin:10px 0}
.news-card .more{font-size:10px;font-weight:600;color:var(--ink)}

/* footer */
.site-footer{left:0;top:5060px;width:1200px;height:324px;background:linear-gradient(180deg,var(--blue-soft),var(--blue))}
.footer-nav{position:absolute;left:0;width:1200px;display:flex;justify-content:center;gap:56px;font-size:12px;color:var(--white)}
.social{position:absolute;top:5316px;width:20px;height:20px;border-radius:50%;background:var(--white)}
</style>
</head>
<body>

<header class="site-header">
  <div class="brand" style="left:128px;top:28px"><span class="mark"></span>Velmora DX</div>
  <nav class="main-nav"><span class="active">Home</span><span>About Us</span><span>Technology</span><span>Science</span><span>Clinical</span><span>News</span></nav>
  <span class="btn btn-yellow" style="left:1004px;top:24px">Contact Us</span>
</header>

<section class="hero">
  <h1 class="abs hero-title">Early Cancer Detection with Confidence</h1>
  <p class="abs p" style="left:128px;top:310px;width:420px">Lorem Ipsum is simply dummy text of the printing and typesetting industry. Lorem Ipsum has been the industry's standard dummy text ever since.</p>
  <span class="btn btn-blue" style="left:128px;top:390px">Learn More</span>
  <div class="photo" role="img" aria-label="Laboratory scientist at work" style="left:800px;top:150px;width:300px;height:300px;border-radius:50%;background:radial-gradient(circle at 40% 40%,#cfe3f5,#6f9fcf)"></div>
  <div class="photo" role="img" aria-label="Molecular science visual" style="left:700px;top:300px;width:200px;height:200px;border-radius:50%;background:radial-gradient(circle,#4c87c9,#1e4e8c);border:6px solid var(--white)"></div>
  <div class="photo" role="img" aria-label="Test tubes in a rack" style="left:990px;top:380px;width:150px;height:150px;border-radius:50%;background:radial-gradient(circle,#e9eef4,#9fb6cf);border:6px solid var(--white)"></div>
  <div class="abs" style="left:780px;top:170px;width:26px;height:26px;border-radius:50%;background:var(--yellow)"></div>
  <div class="abs" style="left:1120px;top:200px;width:18px;height:18px;border-radius:50%;background:var(--blue)"></div>
  <div class="abs" style="left:930px;top:520px;width:22px;height:22px;border-radius:50%;background:var(--yellow)"></div>
  <div class="abs hero-stripe"></div>
</section>

<section class="about">
  <div class="photo" role="img" aria-label="University building facade" style="left:160px;top:640px;width:380px;height:380px;border-radius:50%;background:linear-gradient(180deg,#c9d9ea,#a78f72 55%,#7d6a55);border:8px solid var(--white);box-shadow:0 0 0 2px var(--line)"></div>
  <h2 class="abs h2" style="left:640px;top:672px;width:400px;text-align:center">About Us</h2>
  <p class="abs" style="left:640px;top:728px;width:400px;text-align:center;font-size:13px;font-weight:600;color:var(--ink)">Ashgrove Hollis <span style="color:var(--blue)">University of Dunmere</span></p>
  <p class="abs p" style="left:660px;top:760px;width:420px">Lorem Ipsum is simply dummy text of the printing and typesetting industry. Lorem Ipsum has been the industry's standard dummy text ever since the 1500s, when an unknown printer took a galley of type and scrambled it to make a type specimen book.</p>
  <p class="abs p" style="left:660px;top:850px;width:420px">Lorem Ipsum is simply dummy text of the printing and typesetting industry. Lorem Ipsum has been the industry's standard dummy text ever since the 1500s, when an unknown printer took a galley of type and scrambled it to make a type specimen book.</p>
  <span class="btn btn-yellow" style="left:780px;top:936px">Learn More</span>
</section>

<section class="abs product">
  <h2 class="abs h2" style="left:0;top:34px;width:1200px;text-align:center;color:var(--white)">Product</h2>
  <p class="abs p" style="left:400px;top:84px;width:400px;text-align:center;color:var(--white)">Lorem Ipsum is simply dummy text of the printing and typesetting industry. Lorem Ipsum has been the industry's standard.</p>
</section>
<div class="feature" style="left:220px;top:1266px;width:260px;background:var(--yellow)"><h3>Our Technology</h3><p>Lorem Ipsum is simply dummy text of the printing and typesetting industry.</p></div>
<div class="feature" style="left:170px;top:1378px;width:350px;background:#8ec3f1"><h3>Clinical Evidence</h3><p>Lorem Ipsum is simply dummy text of the printing and typesetting industry.</p></div>
<div class="feature" style="left:130px;top:1490px;width:340px;background:var(--yellow)"><h3>Our University Heritage</h3><p>Lorem Ipsum is simply dummy text of the printing and typesetting industry.</p></div>
<div class="photo" role="img" aria-label="Urine sample test bottle" style="left:500px;top:1258px;width:190px;height:370px;border-radius:40px 40px 30px 30px;background:linear-gradient(90deg,#c7dff4,#ffffff 45%,#9fc4e8)"></div>
<svg class="abs" style="left:680px;top:1450px" width="120" height="110" viewBox="0 0 120 110"><path d="M100 10 C100 70 60 90 12 86" fill="none" stroke="#fff" stroke-width="3"/><path d="M24 76 L10 86 L24 96" fill="none" stroke="#fff" stroke-width="3"/></svg>
<div class="abs product-name">GlandSURE™</div>

<section class="investors">
  <div class="abs" style="left:160px;top:1792px;width:500px;height:310px;background:var(--blue);border-radius:8px"></div>
  <h2 class="abs h2" style="left:200px;top:1830px;color:var(--white)">Investors</h2>
  <p class="abs p" style="left:200px;top:1885px;width:420px;color:var(--white)">Lorem Ipsum is simply dummy text of the printing and typesetting industry. Lorem Ipsum has been the industry's standard dummy text ever since the 1500s, when an unknown printer took a galley of type and scrambled it to make a type specimen book. Lorem Ipsum has been the industry's standard.</p>
  <span class="btn btn-white" style="left:350px;top:2030px">Learn More</span>
  <div class="photo" role="img" aria-label="Business investor smiling" style="left:690px;top:1770px;width:240px;height:240px;border-radius:50%;background:radial-gradient(circle,#a8b4c4,#3b4a5e);border:6px solid var(--white)"></div>
  <div class="photo" role="img" aria-label="Team meeting around a table" style="left:860px;top:1900px;width:180px;height:180px;border-radius:50%;background:radial-gradient(circle,#d8d2c8,#7b7468);border:6px solid var(--white)"></div>
  <div class="photo" role="img" aria-label="Investor reviewing documents" style="left:720px;top:2030px;width:150px;height:150px;border-radius:50%;background:radial-gradient(circle,#c4cfdc,#4e5f75);border:6px solid var(--white)"></div>
</section>

<section class="clinicians">
  <div class="photo" role="img" aria-label="Clinicians discussing results at a desk" style="left:0;top:2260px;width:620px;height:620px;border-radius:0 50% 50% 0;background:linear-gradient(135deg,#efe6dc,#b99a80 60%,#6a5142)"></div>
  <h2 class="abs h2" style="left:700px;top:2360px;width:370px;text-align:center">Clinicians</h2>
  <p class="abs p" style="left:700px;top:2416px;width:370px">Lorem Ipsum is simply dummy text of the printing and typesetting industry. Lorem Ipsum has been the industry's standard dummy text ever since the 1500s, when an unknown printer took a galley of type and scrambled it to make a type specimen book.</p>
  <p class="abs p" style="left:700px;top:2530px;width:370px">Lorem Ipsum is simply dummy text of the printing and typesetting industry. Lorem Ipsum has been the industry's standard dummy text ever since the 1500s, when an unknown printer took a galley of type and scrambled it to make a type specimen book.</p>
  <span class="btn btn-yellow" style="left:820px;top:2640px">Learn More</span>
</section>

<section class="partners">
  <h2 class="abs h2" style="left:160px;top:2950px">Partners</h2>
  <p class="abs p" style="left:160px;top:3004px;width:380px">Lorem Ipsum is simply dummy text of the printing and typesetting industry. Lorem Ipsum has been the industry's standard dummy text ever since the 1500s, when an unknown printer took a galley of type.</p>
  <p class="abs p" style="left:160px;top:3092px;width:380px">Lorem Ipsum is simply dummy text of the printing and typesetting industry. Lorem Ipsum has been the industry's standard dummy text ever since the 1500s, when an unknown printer took a galley of type and scrambled it to make a type specimen book.</p>
  <span class="btn btn-blue" style="left:270px;top:3234px">Learn More</span>
  <div class="photo" role="img" aria-label="Partners shaking hands in an office" style="left:600px;top:2860px;width:640px;height:560px;border-radius:280px 0 0 280px;background:linear-gradient(135deg,#f1f3f6,#9aa3b0 55%,#2f3540);border-left:3px solid var(--blue)"></div>
</section>

<section class="abs testimonials">
  <h2 class="abs h2" style="left:0;top:46px;width:1200px;text-align:center;color:var(--white)">Latest Testimonial</h2>
  <p class="abs" style="left:0;top:98px;width:1200px;text-align:center;font-size:13px;color:#c7cad1">There's a new rise of mild low blood sugar hypoglycemia</p>
</section>
<div class="t-card" style="left:-70px;opacity:.5"><div class="avatar"></div><p>A calm process and a clear result helped our team plan the next steps with ease.</p></div>
<div class="t-card" style="left:190px"><div class="avatar"></div><p>"Clear results and a kind team made every step simple. The test fit neatly into our clinic routine and patients felt cared for from start to finish."</p><div class="name">Talia Brennick</div><div class="role">Clinical Lead</div></div>
<div class="t-card" style="left:480px"><div class="avatar"></div><p>"My team saw real value in the early risk score. Fast turnaround, strong support and data we can trust when we talk to families."</p><div class="name">Orin Castell</div><div class="role">Hospital Partner</div></div>
<div class="t-card" style="left:770px"><div class="avatar"></div><p>"Straightforward, reliable and well explained. The science is solid and the service is friendly, which makes a real difference daily."</p><div class="name">Nadia Voss</div><div class="role">Research Fellow</div></div>
<div class="t-card" style="left:1060px;opacity:.5"><div class="avatar"></div><p>A trusted partner for early screening work.</p></div>
<div class="arrow" style="left:124px"><svg width="30" height="30" viewBox="0 0 30 30"><path d="M17 9 L11 15 L17 21" fill="none" stroke="#fff" stroke-width="2.5"/></svg></div>
<div class="arrow" style="left:1046px"><svg width="30" height="30" viewBox="0 0 30 30"><path d="M13 9 L19 15 L13 21" fill="none" stroke="#fff" stroke-width="2.5"/></svg></div>
<span class="btn btn-blue" style="left:508px;top:3980px">View All Testimonial</span>

<section class="partner-list">
  <h2 class="abs h2" style="left:0;top:4124px;width:1200px;text-align:center">Our Partners</h2>
  <p class="abs p" style="left:0;top:4176px;width:1200px;text-align:center">Lorem Ipsum is simply dummy text of the printing and typesetting industry.</p>
  <div class="abs" style="left:150px;top:4236px;width:130px;height:40px;border-radius:6px;background:#d5dff0"></div>
  <div class="abs" style="left:310px;top:4236px;width:110px;height:40px;border-radius:6px;background:#f4dfc2"></div>
  <div class="abs" style="left:450px;top:4236px;width:130px;height:40px;border-radius:6px;background:#dde3ea"></div>
  <div class="abs" style="left:610px;top:4236px;width:120px;height:40px;border-radius:6px;background:#cfe0f3"></div>
  <div class="abs" style="left:760px;top:4236px;width:110px;height:40px;border-radius:6px;background:#c9d6ee"></div>
  <div class="abs" style="left:900px;top:4236px;width:150px;height:40px;border-radius:6px;background:#d6ecd8"></div>
</section>

<section class="news">
  <h2 class="abs h2" style="left:0;top:4322px;width:1200px;text-align:center">Latest News</h2>
  <p class="abs p" style="left:0;top:4372px;width:1200px;text-align:center">Lorem Ipsum is simply dummy text of the printing and typesetting industry.</p>
  <article class="news-card" style="left:160px">
    <div class="img" role="img" aria-label="Team celebrating an award" style="background:linear-gradient(135deg,#e6e9ee,#7d8694 60%,#3a414d)"></div>
    <div class="meta">JUNE 13, 2025 | 0 COMMENTS</div>
    <h4>Proud to be among the few biotech startups selected for the prestigious Healthtech…</h4>
    <p>Discover the latest trends in hotel architecture and design with insights on the future of hospitality in our blog. The future of hospitality: Trends in hotel architecture.</p>
    <div class="more">LEARN MORE ›</div>
  </article>
  <article class="news-card" style="left:620px">
    <div class="img" role="img" aria-label="Healthcare professionals in discussion" style="background:linear-gradient(135deg,#eef2f6,#9db0c4 60%,#4a5d72)"></div>
    <div class="meta">JUNE 13, 2025 | 0 COMMENTS</div>
    <h4>Proud to be among the few biotech startups selected for the prestigious Healthtech…</h4>
    <p>Discover the latest trends in hotel architecture and design with insights on the future of hospitality in our blog. The future of hospitality: Trends in hotel architecture.</p>
    <div class="more">LEARN MORE ›</div>
  </article>
  <span class="btn btn-yellow" style="left:536px;top:4870px">View All News</span>
</section>

<footer class="abs site-footer">
  <div class="abs" style="left:500px;top:36px;width:200px;height:64px;background:var(--white);border-radius:4px"></div>
  <div class="brand" style="left:528px;top:54px"><span class="mark"></span>Velmora DX</div>
  <nav class="footer-nav" style="top:150px"><span>Home</span><span>About Us</span><span>Technology</span><span>Science</span><span>Clinical</span><span>News</span></nav>
  <nav class="footer-nav" style="top:182px;gap:40px;font-size:11px"><span>Contact Us</span><span>Privacy Policy</span><span>Terms of Use</span></nav>
</footer>
<div class="social" style="left:534px"></div>
<div class="social" style="left:566px"></div>
<div class="social" style="left:598px"></div>
<div class="social" style="left:630px"></div>
<div class="social" style="left:662px"></div>

</body>
</html>
```